Business Card Design - Local Discount Club

Looking for a fun business card for a local discount club. One side should be the logo only and the other should be have :

Name
Title
Phone, Email
Website

```html
<!DOCTYPE html>
<html lang="en">
<head>
<meta charset="utf-8">
<title>Harbor Point Pass – Business Card</title>
<link rel="stylesheet" href="https://fonts.googleapis.com/css2?family=Montserrat:wght@700;800&family=Open+Sans:wght@400&display=swap">
<style>
  :root {
    --backdrop: #c2c3c5;
    --navy: #05235f;
    --royal: #3a5bbf;
    --sky: #3fd6f5;
    --mint: #a8f07a;
    --paper: #ffffff;
    --ink: #111111;
  }
  * { margin: 0; padding: 0; box-sizing: border-box; }
  html, body { width: 900px; height: 1200px; overflow: hidden; }
  body { background: var(--backdrop); position: relative; }

  .card-shapes { position: absolute; inset: 0; }
  .card-front-shape { fill: var(--navy); stroke: var(--navy); }
  .card-back-shape { fill: var(--paper); stroke: var(--paper); }
  .peninsula-map { fill: var(--royal); }

  .logo-lockup {
    position: absolute; left: 240px; top: 340px; width: 440px;
    display: flex; align-items: flex-start; justify-content: space-between; gap: 18px;
  }
  .logo-name {
    font-family: "Montserrat", sans-serif; font-weight: 800;
    font-size: 58px; line-height: 1; color: var(--royal);
    letter-spacing: 1px; text-transform: uppercase;
  }
  .logo-dot {
    width: 26px; height: 26px; border-radius: 50%;
    background: var(--sky); flex: none;
  }

  .holder { position: absolute; left: 234px; top: 694px; }
  .holder-name {
    font-family: "Montserrat", sans-serif; font-weight: 800;
    font-size: 18px; color: var(--sky); letter-spacing: 0.5px;
    text-transform: uppercase; line-height: 1;
  }
  .holder-title {
    font-family: "Open Sans", sans-serif; font-size: 12px;
    color: var(--ink); margin-top: 1px;
  }

  .contact-list {
    position: absolute; left: 234px; top: 852px; list-style: none;
    font-family: "Open Sans", sans-serif; font-size: 12px;
    color: var(--ink); letter-spacing: 0.2px;
  }
  .contact-list li { display: flex; align-items: center; gap: 7px; height: 21px; }
  .contact-list svg { width: 11px; height: 11px; flex: none; }
</style>
</head>
<body>
  <svg class="card-shapes" width="900" height="1200" viewBox="0 0 900 1200">
    <polygon class="card-front-shape" stroke-width="56" stroke-linejoin="round"
             points="250,310 690,246 706,540 216,556"/>
    <polygon class="card-back-shape" stroke-width="56" stroke-linejoin="round"
             points="216,660 640,718 692,930 216,932"/>
    <rect class="peninsula-map" role="img" aria-label="Map silhouette of the coastal peninsula"
          x="425" y="715" width="245" height="240" rx="36"/>
  </svg>

  <div class="logo-lockup">
    <span class="logo-name">Harbor Point Pass</span>
    <span class="logo-dot"></span>
  </div>

  <div class="holder">
    <p class="holder-name">Dana Whitley</p>
    <p class="holder-title">Founder</p>
  </div>

  <ul class="contact-list">
    <li>
      <svg viewBox="0 0 12 12"><path d="M2.5 1 L4.5 1 L5.2 3.6 L3.9 4.5 A6 6 0 0 0 7.5 8.1 L8.4 6.8 L11 7.5 L11 9.5 A1.5 1.5 0 0 1 9.5 11 A8.5 8.5 0 0 1 1 2.5 A1.5 1.5 0 0 1 2.5 1 Z" fill="#3fd6f5"/></svg>
      555-204-7318
    </li>
    <li>
      <svg viewBox="0 0 12 12"><rect x="0.5" y="2" width="11" height="8" fill="#a8f07a"/><path d="M0.5 2 L6 6.5 L11.5 2" stroke="#fff" stroke-width="1" fill="none"/></svg>
      info@harborpointpass.com
    </li>
    <li>
      <svg viewBox="0 0 12 12"><circle cx="6" cy="6" r="5.3" fill="none" stroke="#3a5bbf" stroke-width="1.2"/><ellipse cx="6" cy="6" rx="2.3" ry="5.3" fill="none" stroke="#3a5bbf" stroke-width="1"/><line x1="0.7" y1="6" x2="11.3" y2="6" stroke="#3a5bbf" stroke-width="1"/></svg>
      www.harborpointpass.com
    </li>
  </ul>
</body>
</html>
```